The Wagon Rolls Yonder is a food truck, talent show, fundraiser event.

The Belmere Uplift Foundation is hosting a food truck, talent show, fundraiser called The Wagon Rolls Yonder. We need a flyer designed that incorporates a couple of our existing logos. The theme this year is "Summer Kickoff Jam." The event will be held Wednesday, May 23rd from 3-6 pm at the BRAND NEW Northwind Civic Amphitheater (R). I've included some of our logos to incorporate into the flyer. This event is geared towards kids K-12.

Target Market(s)

Kids (K-12) and parents

Industry/Entity Type

Non Profit

Colors

Designer to choose colors to be used in the design.

Requirements
Must have
• Incorporate both logos: Truck (prominent), Foundation logo (not as prominent).
Nice to have
• Might need to have some space to add sponsor logos. Not a must.

```html
<!DOCTYPE html>
<html lang="en">
<head>
<meta charset="utf-8">
<title>Summer Kickoff Jam Flyer</title>
<link href="https://fonts.googleapis.com/css2?family=Open+Sans:wght@400;700&family=Courgette&family=Great+Vibes&display=swap" rel="stylesheet">
<style>
  :root {
    --coral: #e4605a;
    --coral-soft: #f08a84;
    --navy: #23307a;
    --teal: #2f9fb8;
    --gold: #f0b625;
    --paper: #fbfbfb;
    --backdrop: #e6e6e6;
    --rule: #e6c2bf;
  }
  * { margin: 0; padding: 0; box-sizing: border-box; }
  html, body { width: 1200px; height: 959px; overflow: hidden; }
  body {
    background: var(--backdrop);
    font-family: "Open Sans", Arial, sans-serif;
    position: relative;
  }
  .flyer {
    position: absolute;
    left: 270px; top: 40px;
    width: 660px; height: 880px;
    background: var(--paper);
    overflow: hidden;
    box-shadow: 0 6px 24px rgba(0,0,0,0.15);
  }
  .swoosh { position: absolute; inset: 0; }

  .truck-mark {
    position: absolute; left: 170px; top: 50px;
    display: flex; align-items: center; gap: 10px;
  }
  .truck-mark .dot {
    width: 34px; height: 34px; border-radius: 50%;
    background: var(--teal);
  }
  .truck-mark .name {
    font-weight: 700; font-size: 22px; color: var(--teal);
    width: 170px; line-height: 1.15;
  }
  .host-row {
    position: absolute; left: 36px; top: 175px;
    display: flex; align-items: center; gap: 26px;
  }
  .foundation-mark { display: flex; align-items: center; gap: 8px; }
  .foundation-mark .dot {
    width: 22px; height: 22px; border-radius: 50%; background: var(--gold);
  }
  .foundation-mark .name {
    font-weight: 700; font-size: 13px; color: var(--navy);
    width: 120px; line-height: 1.2;
  }
  .hosting {
    font-family: "Great Vibes", cursive; font-size: 30px; color: #333;
  }

  .highlights {
    position: absolute; left: 400px; top: 40px;
    list-style: none;
    font-family: "Great Vibes", cursive; font-size: 22px;
    color: var(--coral); line-height: 1.45;
  }
  .highlights li::before {
    content: "\2605"; font-family: "Open Sans", sans-serif;
    font-size: 11px; color: var(--coral); margin-right: 8px;
    vertical-align: middle;
  }

  .performer-collage {
    position: absolute; left: 150px; top: 235px;
    width: 350px; height: 200px;
    transform: rotate(-6deg);
    background: linear-gradient(135deg, #3d3d9a 0%, #5a4fb0 35%, #c9a27e 55%, #4b4aa6 80%, #2b2f7e 100%);
    border: 6px solid #fff;
    box-shadow: 0 6px 14px rgba(0,0,0,0.25);
  }

  .title {
    position: absolute; left: 0; right: 0; top: 500px;
    text-align: center;
    font-family: "Courgette", cursive; font-size: 44px; font-weight: 400;
  }
  .title .star { font-family: "Open Sans", sans-serif; font-size: 14px; color: var(--coral); vertical-align: middle; margin: 0 10px; }
  .title .coral { color: var(--coral); }
  .title .navy { color: var(--navy); }
  .title-rule {
    position: absolute; left: 60px; right: 60px; top: 572px;
    height: 1px; background: var(--rule);
  }

  .date-badge { position: absolute; left: 40px; top: 600px; width: 270px; height: 270px; }
  .date-badge svg { position: absolute; inset: 0; }
  .date-badge .text {
    position: absolute; inset: 0;
    display: flex; flex-direction: column; align-items: center; justify-content: center;
    color: #fff; text-align: center;
  }
  .date-badge .stars { font-size: 16px; letter-spacing: 6px; }
  .date-badge .day { font-family: "Courgette", cursive; font-size: 30px; line-height: 1.1; }
  .date-badge .date { font-size: 54px; line-height: 1; }
  .date-badge .from { font-family: "Courgette", cursive; font-size: 16px; }
  .date-badge .time { font-size: 46px; line-height: 1; }

  .venue {
    position: absolute; left: 345px; top: 640px; color: var(--navy);
  }
  .venue .at { font-size: 40px; color: var(--coral); font-weight: 700; line-height: 1; }
  .venue .lead { font-size: 30px; font-weight: 700; line-height: 1.2; }
  .venue .place { font-size: 30px; font-weight: 400; line-height: 1.2; }
</style>
</head>
<body>
  <main class="flyer">
    <svg class="swoosh" viewBox="0 0 660 880" aria-hidden="true">
      <path d="M630 0 C 615 150, 420 290, 230 380 C 140 420, 60 450, 0 468 L 0 505 C 70 488, 160 455, 250 410 C 440 315, 640 170, 660 0 Z" fill="#e4605a" opacity="0.85"/>
    </svg>

    <div class="truck-mark">
      <span class="dot"></span>
      <span class="name">The Wagon Rolls Yonder</span>
    </div>

    <ul class="highlights">
      <li>Food trucks</li>
      <li>Talent show</li>
      <li>Fundraiser</li>
    </ul>

    <div class="host-row">
      <div class="foundation-mark">
        <span class="dot"></span>
        <span class="name">The Belmere Uplift Foundation</span>
      </div>
      <span class="hosting">hosting</span>
    </div>

    <div class="performer-collage" role="img" aria-label="Photo collage of a young performer singing on stage under purple lights"></div>

    <h1 class="title">
      <span class="star">&#9733;</span><span class="coral">Summer</span> <span class="navy">Kickoff</span> <span class="coral">Jam</span><span class="star">&#9733;</span>
    </h1>
    <div class="title-rule"></div>

    <div class="date-badge">
      <svg viewBox="0 0 300 300" aria-hidden="true">
        <g fill="#e4605a">
          <circle cx="150" cy="150" r="122"/>
          <circle cx="150" cy="30" r="16" transform="rotate(0 150 150)"/>
          <circle cx="150" cy="30" r="16" transform="rotate(15 150 150)"/>
          <circle cx="150" cy="30" r="16" transform="rotate(30 150 150)"/>
          <circle cx="150" cy="30" r="16" transform="rotate(45 150 150)"/>
          <circle cx="150" cy="30" r="16" transform="rotate(60 150 150)"/>
          <circle cx="150" cy="30" r="16" transform="rotate(75 150 150)"/>
          <circle cx="150" cy="30" r="16" transform="rotate(90 150 150)"/>
          <circle cx="150" cy="30" r="16" transform="rotate(105 150 150)"/>
          <circle cx="150" cy="30" r="16" transform="rotate(120 150 150)"/>
          <circle cx="150" cy="30" r="16" transform="rotate(135 150 150)"/>
          <circle cx="150" cy="30" r="16" transform="rotate(150 150 150)"/>
          <circle cx="150" cy="30" r="16" transform="rotate(165 150 150)"/>
          <circle cx="150" cy="30" r="16" transform="rotate(180 150 150)"/>
          <circle cx="150" cy="30" r="16" transform="rotate(195 150 150)"/>
          <circle cx="150" cy="30" r="16" transform="rotate(210 150 150)"/>
          <circle cx="150" cy="30" r="16" transform="rotate(225 150 150)"/>
          <circle cx="150" cy="30" r="16" transform="rotate(240 150 150)"/>
          <circle cx="150" cy="30" r="16" transform="rotate(255 150 150)"/>
          <circle cx="150" cy="30" r="16" transform="rotate(270 150 150)"/>
          <circle cx="150" cy="30" r="16" transform="rotate(285 150 150)"/>
          <circle cx="150" cy="30" r="16" transform="rotate(300 150 150)"/>
          <circle cx="150" cy="30" r="16" transform="rotate(315 150 150)"/>
          <circle cx="150" cy="30" r="16" transform="rotate(330 150 150)"/>
          <circle cx="150" cy="30" r="16" transform="rotate(345 150 150)"/>
        </g>
        <circle cx="150" cy="150" r="122" fill="none" stroke="#fff" stroke-width="2" opacity="0.9"/>
      </svg>
      <div class="text">
        <span class="stars">&#9733;&#9733;&#9733;</span>
        <span class="day">Wednesday</span>
        <span class="date">May 23</span>
        <span class="from">From</span>
        <span class="time">3-6pm</span>
      </div>
    </div>

    <div class="venue">
      <div class="at">@</div>
      <div class="lead">BRAND NEW</div>
      <div class="lead">Northwind Civic</div>
      <div class="place">Amphitheater (R)</div>
    </div>
  </main>
</body>
</html>
```